KVRD Pinecrest Rehabilitation Consultants, INC
Business Card and Stationary for KVRD Pinecrest Rehabilitation
Professional
Dorian K. Lumbard, Ph. D.
Vocational Rehabilitation Consultant
4173b GA Hwy 508 STE 612 Conyers, GA 30081
Dorian.Lumbard@kvrdpinecrestrehab.example
www.kvrdpinecrestrehab.example
I will need whole set of stationary, letterhead, envelopes etc.

```html
<!DOCTYPE html>
<html lang="en">
<head>
<meta charset="utf-8">
<title>KVRD Pinecrest Rehabilitation – Business Card</title>
<link rel="stylesheet" href="https://fonts.googleapis.com/css2?family=Open+Sans:wght@400;600&display=swap">
<style>
  :root {
    --backdrop: #e9e9e7;
    --card-dark: #232323;
    --card-dark-edge: #2d2d2d;
    --card-light: #f7f7f7;
    --brand-blue: #2f7fd6;
    --brand-blue-deep: #1f5fc0;
    --ink: #3a3a3a;
    --ink-soft: #6b6b6b;
    --divider: #c9c9c9;
    --mark-grey: #9a9a9a;
    --white: #ffffff;
  }
  * { box-sizing: border-box; margin: 0; padding: 0; }
  html, body { width: 1200px; height: 901px; overflow: hidden; }
  body {
    background: var(--backdrop);
    font-family: "Open Sans", Arial, sans-serif;
    position: relative;
  }
  .card {
    position: absolute;
    left: 280px;
    width: 640px;
    height: 366px;
    border-radius: 4px;
    box-shadow: 0 8px 22px rgba(0,0,0,0.18);
    overflow: hidden;
  }
  .card--front {
    top: 64px;
    background: radial-gradient(ellipse at 50% 45%, var(--card-dark-edge), var(--card-dark) 70%);
    display: flex;
    align-items: center;
    justify-content: center;
  }
  .card--back { top: 470px; background: var(--card-light); }

  .brand { display: flex; align-items: center; gap: 14px; }
  .brand__dot {
    width: 34px; height: 34px; border-radius: 50%;
    background: var(--mark-grey);
    flex: none;
  }
  .brand__name {
    font-weight: 600;
    color: var(--brand-blue);
    letter-spacing: 0.04em;
    line-height: 1.25;
  }
  .card--front .brand__name { font-size: 26px; }

  .back__brand { position: absolute; left: 36px; top: 86px; }
  .back__brand .brand__name { font-size: 19px; max-width: 230px; }
  .back__brand .brand__dot { width: 28px; height: 28px; }

  .back__divider {
    position: absolute; left: 320px; top: 52px;
    width: 1px; height: 150px; background: var(--divider);
  }
  .contact {
    position: absolute; left: 334px; top: 56px; right: 14px;
    list-style: none;
    font-size: 11.5px; color: var(--ink);
    line-height: 1.6;
  }
  .contact li { display: flex; align-items: center; gap: 6px; white-space: nowrap; }
  .contact__address { display: block !important; margin-bottom: 4px; color: var(--ink-soft); }
  .contact svg { width: 11px; height: 11px; flex: none; fill: var(--brand-blue-deep); }

  .back__swoosh { position: absolute; left: 0; bottom: 0; width: 640px; height: 170px; }
  .back__person {
    position: absolute; left: 40px; right: 24px; bottom: 26px;
    color: var(--white); font-size: 13px; letter-spacing: 0.06em;
    white-space: nowrap;
  }
  .back__person-name { font-weight: 600; text-transform: uppercase; }
  .back__person-degree { font-weight: 600; }
</style>
</head>
<body>

  <section class="card card--front" aria-label="Business card front">
    <div class="brand">
      <span class="brand__dot"></span>
      <span class="brand__name">KVRD Pinecrest Rehabilitation</span>
    </div>
  </section>

  <section class="card card--back" aria-label="Business card back">
    <div class="brand back__brand">
      <span class="brand__dot"></span>
      <span class="brand__name">KVRD Pinecrest Rehabilitation</span>
    </div>

    <div class="back__divider"></div>

    <ul class="contact">
      <li class="contact__address">4173b GA Hwy 508 STE 612<br>Conyers, GA 30081</li>
      <li>
        <svg viewBox="0 0 24 24"><path d="M6.6 10.8a15.1 15.1 0 0 0 6.6 6.6l2.2-2.2a1 1 0 0 1 1-.25 11.4 11.4 0 0 0 3.6.57 1 1 0 0 1 1 1V20a1 1 0 0 1-1 1A17 17 0 0 1 3 4a1 1 0 0 1 1-1h3.5a1 1 0 0 1 1 1 11.4 11.4 0 0 0 .57 3.6 1 1 0 0 1-.25 1z"/></svg>
        012 555 0147
      </li>
      <li>
        <svg viewBox="0 0 24 24"><path d="M2 5h20v14H2z M2 5l10 8 10-8" fill="none" stroke="#1f5fc0" stroke-width="2.4"/></svg>
        Dorian.Lumbard@kvrdpinecrestrehab.example
      </li>
      <li>
        <svg viewBox="0 0 24 24"><circle cx="12" cy="12" r="10"/></svg>
        www.kvrdpinecrestrehab.example
      </li>
    </ul>

    <svg class="back__swoosh" viewBox="0 0 640 170" preserveAspectRatio="none" aria-hidden="true">
      <defs>
        <linearGradient id="bandBlue" x1="0" y1="0" x2="1" y2="0">
          <stop offset="0" stop-color="#1f5fc0"/>
          <stop offset="1" stop-color="#4a9be8"/>
        </linearGradient>
      </defs>
      <path d="M0 110 C 180 120, 420 70, 640 10 L 640 170 L 0 170 Z" fill="url(#bandBlue)"/>
      <path d="M0 96 C 200 112, 430 62, 640 -2" fill="none" stroke="#1a1a1a" stroke-width="5"/>
      <path d="M0 103 C 190 116, 425 66, 640 4" fill="none" stroke="#ffffff" stroke-width="4"/>
    </svg>

    <p class="back__person"><span class="back__person-name">Dorian K. Lumbard</span><span class="back__person-degree">, Ph. D.</span> Vocational Rehabilitation Consultant</p>
  </section>

</body>
</html>
```